Copper Heron need a Recruitment ad poster design

We need a poster design to hire a high end sampling team. our target is university students. The message/ad must be witty, challenging, clever, curious, extremely creative and funny.

We need to entice their curiosity about the job and make them apply. The job is offering an attractive salary, learning experience, fun and exposure for students

Target Market(s)

Our target are males and females who are:
Ambitious, Life loving, Great common sense, Smart,Energetic, Social butterfly, Social Intelligence, Individualistic, Dynamic, Committed & Responsible, Passionate, Chameleon, Have great hair, Intelligent
Confident, Beautiful, Charming, Adventurous, Athletic.
Boys should be: "WORK HARD, PLAY HARD", GREAT NET-WORKER
BARNABY QUILLFEATHER :)

Industry/Entity Type

University

Font styles to use
Decorative
Other font styles liked:
• Stylus BT

Requirements
Must have
• Fun and witty message
Should not have
• people wearing suits!
The title "hiring ad"

```html
<!DOCTYPE html>
<html lang="en">
<head>
<meta charset="utf-8">
<title>Copper Heron – Hiring Poster</title>
<link href="https://fonts.googleapis.com/css2?family=Varela+Round&family=Rock+Salt&family=Arimo:wght@700&display=swap" rel="stylesheet">
<style>
  :root {
    --backdrop: #e9e8e6;
    --poster-red: #b01f24;
    --band-red: #9b1a1e;
    --sun-yellow: #f0b23a;
    --stripe-orange: #d8452a;
    --stripe-dark: #9a1b1c;
    --outline-red: #8c1a19;
    --halo-orange: #e26a2c;
    --ink-white: #ffffff;
  }
  * { margin: 0; padding: 0; box-sizing: border-box; }
  html, body {
    width: 1200px; height: 1148px; overflow: hidden;
    background: var(--backdrop);
  }
  .poster {
    position: absolute; left: 210px; top: 36px;
    width: 780px; height: 1076px;
    background: var(--poster-red);
    overflow: hidden;
  }
  .poster-shapes { position: absolute; inset: 0; }
  .headline {
    position: absolute; left: 0; width: 760px; top: 290px;
    text-align: center;
    font-family: "Varela Round", sans-serif;
    font-size: 76px; line-height: 108px;
    color: var(--ink-white);
    -webkit-text-stroke: 10px var(--outline-red);
    paint-order: stroke fill;
    text-shadow: 0 0 0 var(--halo-orange), 3px 3px 0 var(--halo-orange), -3px -3px 0 var(--halo-orange);
    transform: rotate(-1.5deg);
  }
  .headline span { display: block; }
  .teaser {
    position: absolute; left: 116px; top: 628px;
    font-family: "Rock Salt", cursive;
    font-size: 25px; line-height: 42px;
    color: var(--ink-white);
    text-transform: uppercase;
    transform: rotate(-3deg);
    transform-origin: left top;
  }
  .job-copy {
    position: absolute; left: 130px; top: 770px; width: 480px;
    font-family: "Arimo", Arial, sans-serif; font-weight: 700;
    font-size: 23px; line-height: 30px;
    color: var(--ink-white);
    text-align: justify;
    transform: rotate(-2.5deg);
    transform-origin: left top;
  }
  .contact-band {
    position: absolute; left: 0; right: 0; bottom: 0; height: 150px;
    background: var(--band-red);
  }
  .contact {
    position: absolute; left: 145px; top: 950px;
    font-family: "Arimo", Arial, sans-serif; font-weight: 700;
    font-size: 23px; line-height: 34px;
    color: var(--ink-white);
    transform: rotate(-1.5deg);
    transform-origin: left top;
  }
</style>
</head>
<body>
  <main class="poster">
    <div class="contact-band"></div>
    <svg class="poster-shapes" width="780" height="1076" viewBox="0 0 780 1076">
      <defs>
        <linearGradient id="stripeFade" x1="0" y1="0" x2="0" y2="1">
          <stop offset="0" stop-color="var(--stripe-orange)" stop-opacity="0"/>
          <stop offset="0.4" stop-color="var(--stripe-orange)" stop-opacity="0.8"/>
          <stop offset="1" stop-color="var(--stripe-orange)" stop-opacity="0.9"/>
        </linearGradient>
        <linearGradient id="stripeDarkFade" x1="0" y1="0" x2="0" y2="1">
          <stop offset="0" stop-color="var(--stripe-dark)" stop-opacity="0.9"/>
          <stop offset="1" stop-color="var(--stripe-dark)" stop-opacity="0.3"/>
        </linearGradient>
      </defs>
      <rect class="accent-stripe" x="168" y="20" width="44" height="420" fill="url(#stripeFade)"/>
      <circle class="sun-disc" cx="450" cy="495" r="292" fill="var(--sun-yellow)"/>
      <rect class="drop-line" x="596" y="600" width="26" height="476" fill="url(#stripeDarkFade)"/>
    </svg>

    <h1 class="headline">
      <span>Prvoe taht</span>
      <span>ure nto</span>
      <span>a cmpouetr</span>
    </h1>

    <p class="teaser">If you can read<br>this please<br>apply now.</p>

    <p class="job-copy">Copper Heron Marketing is hiring university students (girls &amp; boys) in the field of sampling. If you like to Play hard and work hard don't hesitate to</p>

    <p class="contact">contact us: 0785642318 or<br>info@copper-heron.com</p>
  </main>
</body>
</html>
```